Packaging Design Project for Coffee Products

Mirelle Cup is a new start-up specialising in Kopi Luwak (dubbed the most expensive coffee in the world). Due to the nature of our product, we would like to provide the premium experience and the first impression often begins with the packaging.

Our target audience is HNWs (high net-worth individuals), coffee connoisseurs, premium restaurants, cafes, and hotels. They are price insensitive and place high importance on quality and service.

We seek to have the packaging design and graphics that is artistic, clean, simple but sophisticated – representing our luxury product and premium service.

We have already thought about the packaging designs but need help when it comes to graphics and placements of information etc. Basically the packaging will consist of inner (aluminium vacuum sealed coffee pouch) and outer (paper tube) packagings.

For our detailed design specification and our logo (in EPS), please download attached files.
Updates

A number of you asked what type of font is used in the logo. The name is Philosopher. 

Project Deadline Extended
Reason: We are extending deadline by a week because we are close but not there yet. Hopefully this time extension will allow designers to tweak further their designs and submit new designs. Thanks for your understanding and cooperation. Regards MirelleCup.

Target Market(s)

HNWs (high net-worth individuals), coffee connoisseurs, premium restaurants, cafes, and hotels. They are price insensitive and place high importance o

Industry/Entity Type

Product

Requirements
Must have
• -design must be scalable as we are not yet 100% fixed on dimensions, we have provided initial reference
-please refer to our design brief for details
Should not have
• -colourful splashes
-extremely big fonts and complicated designs
-

```html
<!DOCTYPE html>
<html lang="en">
<head>
<meta charset="utf-8">
<title>Mirelle Cup – Kopi Luwak Packaging</title>
<link href="https://fonts.googleapis.com/css2?family=Philosopher:wght@400;700&family=Cormorant+Garamond:wght@500;600&family=Petit+Formal+Script&display=swap" rel="stylesheet">
<style>
  :root {
    --bg: #ffffff;
    --cream: #f6f3ec;
    --map-beige: #cdbfa5;
    --espresso: #2f1a10;
    --roast: #5a3a24;
    --mocha: #7a5236;
    --band: #1e120b;
    --parchment: #d9c7a4;
    --parchment-dark: #b89e74;
    --gold: #e9c15a;
    --ink: #3a2616;
    --light-text: #e8dccb;
    --flag-red: #d0202a;
  }
  * { box-sizing: border-box; margin: 0; padding: 0; }
  html, body { width: 1200px; height: 882px; overflow: hidden; background: var(--bg); }
  .canvas { position: relative; width: 1200px; height: 882px; font-family: 'Cormorant Garamond', serif; }

  /* pouch top label */
  .pouch-label {
    position: absolute; left: 357px; top: 0; width: 569px; height: 255px;
    background: var(--cream);
  }
  .pouch-label__map {
    position: absolute; left: 30px; top: 40px; width: 500px; height: 175px;
    background: radial-gradient(ellipse at 55% 50%, var(--map-beige), rgba(205,191,165,0.35) 70%, transparent 80%);
  }
  .pouch-label__brand {
    position: absolute; left: 0; right: 0; top: 120px; text-align: center;
    font-family: 'Philosopher', sans-serif; font-size: 15px; color: var(--roast);
  }

  /* tube lid */
  .lid {
    position: absolute; left: 927px; top: 3px; width: 186px; height: 186px; border-radius: 50%;
    background: var(--roast); display: flex; align-items: center; justify-content: center;
  }
  .lid__inner {
    width: 160px; height: 160px; border-radius: 50%;
    background: radial-gradient(circle at 50% 40%, #4a2d1b, var(--espresso));
    display: flex; flex-direction: column; align-items: center; padding-top: 34px;
  }
  .product-title { color: var(--gold); text-align: center; line-height: 1.05; font-weight: 600; }
  .lid .product-title__line1 { font-size: 18px; }
  .lid .product-title__line2 { font-size: 24px; }
  .lid__brand { margin-top: 16px; font-family: 'Philosopher', sans-serif; font-size: 12px; color: var(--light-text); }

  /* tube wrap */
  .wrap {
    position: absolute; left: 346px; top: 302px; width: 854px; height: 569px; overflow: hidden;
    background: linear-gradient(to bottom, #3b2416 0%, var(--mocha) 20%, var(--roast) 55%, var(--espresso) 100%);
  }
  .wrap__band { position: absolute; left: 0; right: 0; top: 134px; height: 64px; background: var(--band); }
  .wrap__map {
    position: absolute; left: 390px; top: 20px; width: 360px; height: 150px;
    background: radial-gradient(ellipse, rgba(232,220,203,0.14), transparent 70%);
  }
  .wrap__compass {
    position: absolute; left: 745px; top: 40px; width: 74px; height: 74px; border-radius: 50%;
    background: radial-gradient(circle, rgba(232,220,203,0.35), rgba(232,220,203,0.05) 70%);
  }
  .story {
    position: absolute; left: 196px; top: 0; width: 180px; height: 569px;
    background: linear-gradient(to right, var(--parchment-dark), var(--parchment) 20%, var(--parchment) 80%, var(--parchment-dark));
  }
  .story__text {
    position: absolute; left: 14px; right: 12px; top: 205px;
    font-family: 'Petit Formal Script', cursive; font-size: 7.6px; line-height: 1.55; color: var(--ink);
  }
  .story__text p + p { margin-top: 9px; }

  .wrap .product-title { position: absolute; left: 660px; top: 206px; width: 190px; }
  .wrap .product-title__line1 { font-size: 22px; }
  .wrap .product-title__line2 { font-size: 30px; }
  .tagline {
    position: absolute; left: 660px; top: 300px; width: 150px; padding: 8px 6px;
    border: 1px solid var(--gold); text-align: center;
    font-family: 'Petit Formal Script', cursive; font-size: 8px; line-height: 1.5; color: var(--light-text);
  }
  .wrap__brand {
    position: absolute; left: 676px; top: 448px; width: 120px; text-align: center;
    font-family: 'Philosopher', sans-serif; font-size: 19px; color: var(--light-text);
  }
  .importer {
    position: absolute; left: 488px; top: 400px; font-size: 9px; line-height: 1.25; color: var(--light-text);
  }
  .web { position: absolute; left: 512px; bottom: 12px; font-size: 11px; color: var(--light-text); }
  .net-weight { position: absolute; right: 12px; bottom: 12px; font-size: 11px; color: var(--light-text); }
  .origin {
    position: absolute; left: 14px; bottom: 32px; display: flex; align-items: center; gap: 6px;
    font-size: 10px; line-height: 1.1; color: var(--light-text);
  }
  .origin__flag { width: 22px; height: 14px; background: linear-gradient(var(--flag-red) 50%, #fff 50%); }
</style>
</head>
<body>
<div class="canvas">

  <section class="pouch-label">
    <div class="pouch-label__map" role="img" aria-label="Faint map of the Indonesian archipelago"></div>
    <div class="pouch-label__brand">MirelleCup</div>
  </section>

  <section class="lid">
    <div class="lid__inner">
      <div class="product-title">
        <div class="product-title__line1">100% Authentic</div>
        <div class="product-title__line2">Kopi Luwak</div>
      </div>
      <div class="lid__brand">MirelleCup</div>
    </div>
  </section>

  <section class="wrap">
    <div class="wrap__map" role="img" aria-label="Faint outline map of Southeast Asia"></div>
    <div class="wrap__compass" role="img" aria-label="Compass rose"></div>
    <div class="wrap__band"></div>

    <div class="story" role="img" aria-label="Torn parchment paper strip">
      <div class="story__text">
        <p>From the archipelago of Indonesia, MirelleCup brings you the finest rarest coffee on the planet – Kopi Luwak.</p>
        <p>Of course, we can't do this alone – thanks to Luwak (Asian Civet) who not only pick the ripest and reddest coffee cherries, passes them through their digestive system and produce the unique taste through enzyme fermentation.</p>
        <p>We carefully clean and select individual beans. We then roast them to perfection (light to medium roast) to bring out their full-bodied, distinct flavours, their rich aroma as well as their smooth and clean lingering aftertaste.</p>
        <p>We want to share with you what we cherish, savour and venerate – the premium gourmet coffee experience.</p>
      </div>
    </div>

    <div class="product-title">
      <div class="product-title__line1">100% Authentic</div>
      <div class="product-title__line2">Kopi Luwak</div>
    </div>
    <div class="tagline">a Premium Gourmet<br>Coffee Experience</div>

    <div class="importer">Importer<br>1-800-555-0147<br>PO Box 2210<br>Harbor City, Florida<br>30021</div>

    <div class="wrap__brand">MirelleCup</div>

    <div class="origin"><span>Product of<br>Indonesia</span><span class="origin__flag"></span></div>
    <div class="web">www.mirellecup.com</div>
    <div class="net-weight">Net Weight: 100 gr</div>
  </section>

</div>
</body>
</html>
```